Indian Ethnic Snack Food Company Looking for Packaging Designs to Take Products to Overseas Customer

We are a 14 year old company based in Chikmagalur, India manufacturing and marketing South Indian Ethnic snack food under the Lumo Crest brand. We are looking for designers who can redesign our packaging to appeal to international customers in Australia, EU, US and the Gulf Region..
Designs should speak about Indian tradition while looking trendy, modern and attractive to present day customers. Pictures of product and present packaging design available on our website at www.lumocrest.in
Packaging can be Pillow Pouch, Paper Board Cartons and Stand Up Pouches.
Total 24 Products
Uploaded CorelDraw file containing our Logo.
Uploaded Product Photos and Photos of Packaging with existing Designs incorporating the products photos.
Designers need not stick to the same theme, need out of the box designing to take Indian products to international markets.
Updates
Project Deadline Extended
Reason: Hope the deadline extension will encourage late invitees to submit few designs. All the best.
Target Market(s)
Mostly Ethnic Indians but want others to taste our products
Industry/Entity Type
Marketing
Requirements
Must have
- Product Pictures
Nice to have
- Traditional Indian decorative motifs

```html
<!DOCTYPE html>
<html lang="en">
<head>
<meta charset="utf-8">
<title>Lumo Crest snack pouches</title>
<link rel="stylesheet" href="https://fonts.googleapis.com/css2?family=Merriweather:wght@400;700;900&family=Gochi+Hand&display=swap">
<style>
  :root {
    --canvas: #e4e4e4;
    --pouch-white: #fbfbfb;
    --masala-dark: #5c1a0f;
    --masala-mid: #7d2d17;
    --masala-accent: #d8323a;
    --murukku-dark: #0d2b55;
    --murukku-mid: #16407a;
    --murukku-accent: #2b4f9c;
    --gold: #c9a24a;
    --claim-green: #4f9e2c;
    --claim-green-dark: #2f6e17;
    --claim-text: #1c2b12;
    --ink-light: #ffffff;
  }
  * { box-sizing: border-box; margin: 0; padding: 0; }
  html, body { width: 1200px; height: 816px; overflow: hidden; }
  body { background: var(--canvas); font-family: "Merriweather", Georgia, serif; position: relative; }

  .pouch {
    position: absolute;
    top: 70px;
    width: 430px;
    height: 660px;
    background: var(--pouch-white);
    overflow: hidden;
  }
  .pouch--masala { left: 125px; --dark: var(--masala-dark); --mid: var(--masala-mid); --accent: var(--masala-accent); }
  .pouch--murukku { left: 640px; --dark: var(--murukku-dark); --mid: var(--murukku-mid); --accent: var(--murukku-accent); }

  .pouch__panel { position: absolute; inset: 0; width: 430px; height: 660px; }

  .brand {
    position: absolute;
    left: 115px;
    top: 80px;
    width: 170px;
    text-align: center;
    color: var(--ink-light);
    font-weight: 700;
    font-size: 38px;
    line-height: 42px;
  }

  .product-name {
    position: absolute;
    left: 46px;
    top: 238px;
    width: 222px;
    color: var(--ink-light);
    font-weight: 700;
    line-height: 1;
    white-space: nowrap;
  }
  .product-name__first { display: block; font-size: 52px; letter-spacing: -0.5px; }
  .product-name__second { display: block; font-size: 38px; margin-top: 8px; letter-spacing: -0.3px; }
  .product-tag {
    position: absolute;
    left: 48px;
    top: 352px;
    color: var(--ink-light);
    font-size: 17px;
  }

  .claim {
    position: absolute;
    left: 290px;
    width: 118px;
    height: 36px;
    background: linear-gradient(180deg, var(--claim-green), var(--claim-green-dark));
    color: var(--claim-text);
    font-family: "Gochi Hand", cursive;
    display: flex;
    align-items: center;
    justify-content: center;
    text-align: center;
    border: 2px solid #e8f3d8;
  }
  .claim--cholesterol { top: 238px; font-size: 13px; line-height: 13px; }
  .claim--cholesterol .claim__big { font-size: 22px; margin-right: 3px; }
  .claim--oil { top: 290px; font-size: 20px; }

  .product-photo {
    position: absolute;
    left: 50px;
    top: 385px;
    width: 330px;
    height: 200px;
    border-radius: 40px 40px 165px 165px / 40px 40px 120px 120px;
    background: radial-gradient(ellipse at 50% 25%, #e9a83a 0%, #c77a22 40%, var(--mid) 75%, var(--dark) 100%);
  }
  .pouch--murukku .product-photo {
    background: radial-gradient(ellipse at 50% 22%, #d98a45 0%, #b8642a 38%, #3fa6dc 62%, #1e6fb0 100%);
  }

  .motif {
    position: absolute;
    background: var(--accent);
    opacity: 0.22;
    border-radius: 50% 50% 50% 50% / 60% 60% 40% 40%;
  }
  .motif--top { left: 300px; top: 50px; width: 72px; height: 150px; }
  .motif--bottom { left: 348px; top: 482px; width: 62px; height: 92px; }
</style>
</head>
<body>

  <section class="pouch pouch--masala" aria-label="Masala Kharapuri pouch">
    <svg class="pouch__panel" viewBox="0 0 430 660" aria-hidden="true">
      <path d="M0 0 H285 C270 150 262 250 272 330 C282 420 296 520 302 660 H0 Z" fill="var(--dark)"/>
      <path d="M285 0 C270 150 262 250 272 330 C282 420 296 520 302 660" fill="none" stroke="var(--gold)" stroke-width="3" stroke-dasharray="2 6" stroke-linecap="round"/>
      <path d="M0 0 H430 V16 L420 24 L410 16 L400 24 L390 16 L380 24 L370 16 L360 24 L350 16 L340 24 L330 16 L320 24 L310 16 L300 24 L290 16 L280 24 L270 16 L260 24 L250 16 L240 24 L230 16 L220 24 L210 16 L200 24 L190 16 L180 24 L170 16 L160 24 L150 16 L140 24 L130 16 L120 24 L110 16 L100 24 L90 16 L80 24 L70 16 L60 24 L50 16 L40 24 L30 16 L20 24 L10 16 L0 24 Z" fill="#000" opacity="0.08"/>
      <path d="M0 660 H430 V644 L420 636 L410 644 L400 636 L390 644 L380 636 L370 644 L360 636 L350 644 L340 636 L330 644 L320 636 L310 644 L300 636 L290 644 L280 636 L270 644 L260 636 L250 644 L240 636 L230 644 L220 636 L210 644 L200 636 L190 644 L180 636 L170 644 L160 636 L150 644 L140 636 L130 644 L120 636 L110 644 L100 636 L90 644 L80 636 L70 644 L60 636 L50 644 L40 636 L30 644 L20 636 L10 644 L0 636 Z" fill="#000" opacity="0.08"/>
    </svg>
    <div class="motif motif--top" role="img" aria-label="Red paisley ornament"></div>
    <div class="motif motif--bottom" role="img" aria-label="Red paisley ornament"></div>
    <div class="brand">Lumo<br>Crest</div>
    <h2 class="product-name"><span class="product-name__first">Masala</span><span class="product-name__second">Kharapuri</span></h2>
    <p class="product-tag">liht snack</p>
    <p class="claim claim--cholesterol"><span class="claim__big">0%</span>Cholesterol &amp;<br>Transfats</p>
    <p class="claim claim--oil">Low Oil</p>
    <div class="product-photo" role="img" aria-label="Decorated brown bowl filled with crunchy masala kharapuri"></div>
  </section>

  <section class="pouch pouch--murukku" aria-label="Ribbon Murukku pouch">
    <svg class="pouch__panel" viewBox="0 0 430 660" aria-hidden="true">
      <path d="M0 0 H285 C270 150 262 250 272 330 C282 420 296 520 302 660 H0 Z" fill="var(--dark)"/>
      <path d="M285 0 C270 150 262 250 272 330 C282 420 296 520 302 660" fill="none" stroke="var(--gold)" stroke-width="3" stroke-dasharray="2 6" stroke-linecap="round"/>
      <path d="M0 0 H430 V16 L420 24 L410 16 L400 24 L390 16 L380 24 L370 16 L360 24 L350 16 L340 24 L330 16 L320 24 L310 16 L300 24 L290 16 L280 24 L270 16 L260 24 L250 16 L240 24 L230 16 L220 24 L210 16 L200 24 L190 16 L180 24 L170 16 L160 24 L150 16 L140 24 L130 16 L120 24 L110 16 L100 24 L90 16 L80 24 L70 16 L60 24 L50 16 L40 24 L30 16 L20 24 L10 16 L0 24 Z" fill="#000" opacity="0.08"/>
      <path d="M0 660 H430 V644 L420 636 L410 644 L400 636 L390 644 L380 636 L370 644 L360 636 L350 644 L340 636 L330 644 L320 636 L310 644 L300 636 L290 644 L280 636 L270 644 L260 636 L250 644 L240 636 L230 644 L220 636 L210 644 L200 636 L190 644 L180 636 L170 644 L160 636 L150 644 L140 636 L130 644 L120 636 L110 644 L100 636 L90 644 L80 636 L70 644 L60 636 L50 644 L40 636 L30 644 L20 636 L10 644 L0 636 Z" fill="#000" opacity="0.08"/>
    </svg>
    <div class="motif motif--top" role="img" aria-label="Blue paisley ornament"></div>
    <div class="motif motif--bottom" role="img" aria-label="Blue paisley ornament"></div>
    <div class="brand">Lumo<br>Crest</div>
    <h2 class="product-name"><span class="product-name__first">Ribbon</span><span class="product-name__second">Murukku</span></h2>
    <p class="product-tag">liht snack</p>
    <p class="claim claim--cholesterol"><span class="claim__big">0%</span>Cholesterol &amp;<br>Transfats</p>
    <p class="claim claim--oil">Low Oil</p>
    <div class="product-photo" role="img" aria-label="Decorated blue bowl filled with crisp ribbon murukku"></div>
  </section>

</body>
</html>
```